Boutique Financial Services/Advisor Business Needs Web Design

Looking for an informational and functional web design for my Financial Services/Financial Advisement business. It should have functionality for Company name, address, phone #, "About Us", Who we are, Our Mission, Services we offer, Biographies/Photos of/about "The Team", and possibly a link to "Contact Us". Would like to see something new & exciting blended with a traditional/professional look that will appeal to those approaching retirement, as well as those younger clients that are beginning to think about planning for the future. I already have a web domain through HostMeadow, but would like this to be the design we use for that domain.
Financial Services/Financial Advisor
Coded - Design and coding required
1 page

```html
<!DOCTYPE html>
<html lang="en">
<head>
<meta charset="utf-8">
<title>Summitline Wealth Management</title>
<link rel="stylesheet" href="https://fonts.googleapis.com/css2?family=Cinzel:wght@400;500&family=Figtree:wght@400;500;600&display=swap">
<style>
:root{
  --navy:#16145c;
  --blue:#0b4ea2;
  --ice:#e8eef6;
  --mist:#f1f1f1;
  --white:#ffffff;
  --ink:#2b2b3a;
  --muted:#6b6b78;
}
*{margin:0;padding:0;box-sizing:border-box}
html,body{width:1200px;height:4684px;overflow:hidden}
body{position:relative;font-family:"Figtree",sans-serif;color:var(--ink);background:var(--white)}
.abs{position:absolute}
.eyebrow{font-size:17px;color:var(--muted);letter-spacing:.3px;text-transform:uppercase}
.section-title{font-family:"Cinzel",serif;font-size:38px;color:var(--navy);font-weight:400}
.center{left:0;width:1200px;text-align:center}

/* header */
.site-header{left:0;top:0;width:1200px;height:138px;background:var(--white)}
.wordmark{display:flex;align-items:center;gap:10px;font-family:"Figtree",sans-serif;font-weight:600;white-space:nowrap}
.wordmark-square{width:18px;height:18px;background:currentColor}
.brand{left:112px;top:56px;font-size:22px;color:var(--navy)}
.topline{right:112px;top:22px;font-size:17px;color:var(--ink);display:flex;align-items:center;gap:10px}
.topline svg{width:15px;height:15px;fill:var(--blue)}
.main-nav{right:112px;top:68px;display:flex;align-items:center;gap:40px;font-size:18px}
.btn-contact{background:var(--blue);color:var(--white);padding:0 18px;height:52px;line-height:52px;font-weight:500;font-size:18px}

/* hero */
.hero{left:0;top:138px;width:1200px;height:782px;overflow:hidden}
.hero-photo{position:absolute;inset:0;background:linear-gradient(160deg,#3d4e66 0%,#27364d 35%,#6a7d97 60%,#c9d3df 85%,#e9edf2 100%)}
.hero-title{position:absolute;left:0;top:114px;width:1200px;text-align:center;font-family:"Cinzel",serif;font-weight:400;color:var(--white);font-size:62px;line-height:80px;text-shadow:0 2px 10px rgba(0,0,0,.35)}
.hero-shape{position:absolute;left:0;top:0}

/* about */
.about{left:0;top:920px;width:1200px;height:800px;background:linear-gradient(var(--ice) 70%,var(--mist))}
.about-label{left:112px;top:44px}
.about-title{left:112px;top:80px;font-family:"Cinzel",serif;font-weight:400;font-size:36px;line-height:48px;color:var(--navy)}
.about-text{left:112px;top:206px;width:485px;font-size:14.5px;line-height:26px;color:#3a3a48}
.video-link{left:112px;top:410px;display:flex;align-items:center;gap:14px;color:var(--blue);font-size:17px;font-weight:500}
.play{width:58px;height:58px;border-radius:50%;background:var(--white);border:5px solid #c9cde0;display:flex;align-items:center;justify-content:center}
.about-photo{left:651px;top:21px;width:438px;height:426px;background:linear-gradient(135deg,#8a8f96,#c9b9a6 45%,#6c7a8e);box-shadow:0 8px 24px rgba(0,0,0,.15)}
.about-band{position:absolute;left:59px;top:0;width:69px;height:426px;background:#34305f}
.about-band span{position:absolute;left:50%;top:50%;transform:translate(-50%,-50%) rotate(-90deg);color:var(--white);font-size:36px;letter-spacing:6px;font-weight:600;white-space:nowrap}

.mission{left:112px;top:1475px;width:977px;height:258px;background:var(--white);box-shadow:0 6px 24px rgba(20,20,60,.06);text-align:center}
.mission h3{margin-top:50px;font-size:23px;color:var(--navy);font-weight:600}
.mission p{margin:22px auto 0;width:780px;font-size:18px;line-height:34px;color:#33333f}

/* services */
.services{left:0;top:1720px;width:1200px;height:975px;background:var(--mist)}
.tab{top:243px;width:175px;height:95px;background:var(--white);border-radius:4px;display:flex;align-items:center;justify-content:center;text-align:center;font-size:19px;line-height:27px;color:#333}
.tab.active{background:var(--navy);color:var(--white)}
.tab.faded{color:#bbb;background:#f8f8f8}
.service-photo{left:112px;top:417px;width:488px;height:469px;background:linear-gradient(120deg,#7e7a60,#b4b09c 45%,#8d8f8a 70%,#5b5d5e)}
.service-title{left:662px;top:430px;font-size:32px;color:var(--ink);font-weight:500}
.service-text{left:662px;top:538px;width:430px;font-size:14.5px;line-height:26px;color:#3a3a48}
.service-text p+p{margin-top:24px}

/* team */
.team{left:0;top:2695px;width:1200px;height:655px;background:var(--white)}
.member{top:230px;width:226px;text-align:center}
.member-photo{width:226px;height:270px;background:linear-gradient(#e3e9f2,#cfd8e5)}
.member-name{margin-top:22px;font-size:20px;font-weight:600;color:var(--ink)}
.member-role{margin-top:6px;font-size:15px;color:var(--muted)}

/* contact */
.contact{left:0;top:3350px;width:1200px;height:820px;background:linear-gradient(var(--ice) 75%,var(--white))}
.field{height:46px;background:var(--white);border:1px solid #dfe4ec;font-size:15px;color:#555;padding:14px 16px}
.submit{left:540px;top:550px;width:120px;height:55px;background:var(--blue);color:var(--white);font-weight:600;font-size:17px;display:flex;align-items:center;justify-content:center}

/* footer */
.footer-shape{left:0;top:4130px}
.footer-brand{left:0;top:4330px;width:1200px;display:flex;justify-content:center}
.footer-brand .wordmark{font-size:34px;color:var(--white);gap:14px}
.footer-brand .wordmark-square{width:26px;height:26px}
.footer-nav{left:0;top:4438px;width:1200px;display:flex;justify-content:center;gap:26px;color:var(--white);font-size:16px;font-weight:500}
.footer-nav i{font-style:normal;opacity:.8}
.rule{left:112px;width:977px;height:1px;background:rgba(255,255,255,.3)}
.info{top:4528px;display:flex;align-items:center;gap:18px;color:var(--white);font-size:15px;line-height:24px}
.info .dot{width:44px;height:44px;border-radius:50%;background:var(--white);display:flex;align-items:center;justify-content:center}
.info .dot svg{width:20px;height:20px;fill:var(--blue)}
.copyright{left:112px;top:4645px;color:var(--white);font-size:14px}
.social{right:112px;top:4633px;display:flex;gap:10px}
.social span{width:38px;height:38px;border-radius:50%;border:1px solid rgba(255,255,255,.8)}
</style>
</head>
<body>

<header class="site-header abs">
  <div class="brand wordmark abs"><span class="wordmark-square"></span><span>Summitline Wealth</span></div>
  <div class="topline abs">
    <svg viewBox="0 0 24 24"><path d="M6.6 10.8a15.1 15.1 0 0 0 6.6 6.6l2.2-2.2c.3-.3.7-.4 1-.2 1.1.4 2.3.6 3.6.6.6 0 1 .4 1 1V20c0 .6-.4 1-1 1A17 17 0 0 1 3 4c0-.6.4-1 1-1h3.5c.6 0 1 .4 1 1 0 1.3.2 2.5.6 3.6.1.3 0 .7-.2 1z"/></svg>
    <span>1 888 888 8888</span><span style="color:#999">|</span>
    <svg viewBox="0 0 24 24"><path d="M2 5h20v14H2z M2 5l10 8 10-8" stroke="#fff" stroke-width="1.5"/></svg>
    <span>hello@summitlinewealth.example</span>
  </div>
  <nav class="main-nav abs">
    <span>About Us</span><span>Services we offer</span><span>The Team</span>
    <span class="btn-contact">CONTACT US</span>
  </nav>
</header>

<section class="hero abs">
  <div class="hero-photo" role="img" aria-label="Advisor reviewing pie charts and financial reports at a desk with a keyboard"></div>
  <h1 class="hero-title">Guiding You to your<br>financial summit</h1>
  <svg class="hero-shape" width="1200" height="782" viewBox="0 0 1200 782">
    <polygon points="0,702 600,474 1200,702 1200,782 0,782" fill="#ffffff"/>
    <polygon points="0,718 600,587 1200,718 1200,782 0,782" fill="#e8eef6" opacity=".7"/>
    <polygon points="60,782 600,587 1140,782" fill="#e8eef6"/>
  </svg>
</section>

<section class="about abs">
  <div class="about-label eyebrow abs">Who we are</div>
  <h2 class="about-title abs">Welcome to Summitline<br>Wealth Management</h2>
  <p class="about-text abs">Sed ut perspiciatis unde omnis iste natus error sit voluptatem accus antium doloremque laudantium, totam rem aperiam, eaque ipsa qu ae ab illo inventore veritatis et quasi architecto beatae vitae dictal sunt explicabo. Nemo enim ipsam voluptatem quia voluptas sit asp ernatur aut odit aut fugit, sed quia consequuntur magni dolores eos qui ratione voluptatem sequi nesciunt</p>
  <div class="video-link abs">
    <span class="play"><svg width="18" height="20" viewBox="0 0 18 20"><polygon points="2,1 17,10 2,19" fill="#16145c"/></svg></span>
    <span>WATCH OUR VIDEO</span>
  </div>
  <div class="about-photo abs" role="img" aria-label="Smiling couple looking at a laptop together">
    <div class="about-band"><span>ABOUT US</span></div>
  </div>
</section>

<div class="mission abs">
  <h3>OUR MISSION</h3>
  <p>Totam rem aperiam, eaque ipsa qu ae ab illo inventore veritatis et quasi architecto beatae vitae dictal sunt explicabo. Nemo enim ipsam voluptatem quia voluptas sit asp ernatur aut odit aut fugit, sed quia consequuntur magni dolores eo.</p>
</div>

<section class="services abs">
  <div class="eyebrow abs center" style="top:90px">What we do</div>
  <h2 class="section-title abs center" style="top:128px">Services We Offer</h2>
  <div class="tab faded abs" style="left:-91px">Asset<br>Protection</div>
  <div class="tab abs" style="left:112px">Wealth<br>Management</div>
  <div class="tab abs" style="left:312px">Financial<br>Planning</div>
  <div class="tab active abs" style="left:513px">Retirement<br>Planning</div>
  <div class="tab abs" style="left:713px">Estate<br>Planning</div>
  <div class="tab abs" style="left:913px">Tax<br>Planning</div>
  <div class="tab faded abs" style="left:1113px">Employee<br>benefits</div>
  <div class="service-photo abs" role="img" aria-label="Retired couple walking together outdoors"></div>
  <h3 class="service-title abs">Retirement Planning</h3>
  <div class="service-text abs">
    <p>Neque porro quisquam est, qui dolorem ipsum quia dolor sit amet, consectetur, adipisci velit, sed quia non numquam eius modi tempora incidunt ut labore et dolore magnam aliquam quaerat voluptatem.</p>
    <p>Ut enim ad minima veniam, quis nostr exercitationem ullam corporis suscipit laboriosam, nisi ut aliquid ex ea commodi consequatur? Quis autem vel eum iure reprehenderit qui in ea voluptate velit esse quam nihil molestiae consequatur, vel illum qui dolorem eum fugiat quo voluptas nulla pariatu per spiciatis unde omnis iste natus.</p>
  </div>
</section>

<section class="team abs">
  <div class="eyebrow abs center" style="top:90px">Meet our team</div>
  <h2 class="section-title abs center" style="top:128px">The Team</h2>
  <div class="member abs" style="left:112px"><div class="member-photo" role="img" aria-label="Portrait of a team member in a dark suit"></div><div class="member-name">Staff Name</div><div class="member-role">CEO</div></div>
  <div class="member abs" style="left:362px"><div class="member-photo" role="img" aria-label="Portrait of a team member in a white blouse"></div><div class="member-name">Staff Name</div><div class="member-role">CEO</div></div>
  <div class="member abs" style="left:612px"><div class="member-photo" role="img" aria-label="Portrait of a team member in a dark suit"></div><div class="member-name">Staff Name</div><div class="member-role">CEO</div></div>
  <div class="member abs" style="left:862px"><div class="member-photo" role="img" aria-label="Portrait of a team member in a navy blazer"></div><div class="member-name">Staff Name</div><div class="member-role">CEO</div></div>
</section>

<section class="contact abs">
  <div class="eyebrow abs center" style="top:100px">Contact us</div>
  <h2 class="section-title abs center" style="top:138px">Get In Touch</h2>
  <div class="field abs" style="left:202px;top:240px;width:390px">First Name</div>
  <div class="field abs" style="left:608px;top:240px;width:390px">Last Name</div>
  <div class="field abs" style="left:202px;top:305px;width:390px">Email Address</div>
  <div class="field abs" style="left:608px;top:305px;width:390px">Phone Number</div>
  <div class="field abs" style="left:202px;top:370px;width:796px;height:125px">Message</div>
  <div class="submit abs">SUBMIT</div>
</section>

<svg class="footer-shape abs" width="1200" height="554" viewBox="0 0 1200 554">
  <polygon points="0,135 600,30 1200,135 1200,554 0,554" fill="#16145c"/>
  <polygon points="0,180 0,135 600,30 1200,135 1200,180 1150,150 600,60 50,150" fill="#ffffff"/>
</svg>
<div class="footer-brand abs">
  <div class="wordmark"><span class="wordmark-square"></span><span>Summitline Wealth</span></div>
</div>
<nav class="footer-nav abs">
  <span>HOME</span><i>|</i><span>ABOUT US</span><i>|</i><span>SERVICES WE OFFER</span><i>|</i><span>THE TEAM</span><i>|</i><span>CONTACT US</span>
</nav>
<div class="rule abs" style="top:4505px"></div>
<div class="info abs" style="left:140px">
  <span class="dot"><svg viewBox="0 0 24 24"><path d="M12 2a7 7 0 0 0-7 7c0 5 7 13 7 13s7-8 7-13a7 7 0 0 0-7-7zm0 9.5A2.5 2.5 0 1 1 12 6a2.5 2.5 0 0 1 0 5.5z"/></svg></span>
  <span>lorem 1123 Maple Crest Road, Suite<br>Dayton, OH</span>
</div>
<div class="info abs" style="left:498px">
  <span class="dot"><svg viewBox="0 0 24 24"><path d="M6.6 10.8a15.1 15.1 0 0 0 6.6 6.6l2.2-2.2c.3-.3.7-.4 1-.2 1.1.4 2.3.6 3.6.6.6 0 1 .4 1 1V20c0 .6-.4 1-1 1A17 17 0 0 1 3 4c0-.6.4-1 1-1h3.5c.6 0 1 .4 1 1 0 1.3.2 2.5.6 3.6.1.3 0 .7-.2 1z"/></svg></span>
  <span>Phone<br>1 888 888 8888</span>
</div>
<div class="info abs" style="left:738px">
  <span class="dot"><svg viewBox="0 0 24 24"><path d="M3 5h18v14H3z"/><path d="M3 5l9 7 9-7" stroke="#fff" stroke-width="1.6" fill="none"/></svg></span>
  <span>Email<br>hello@summitlinewealth.example</span>
</div>
<div class="rule abs" style="top:4615px"></div>
<div class="copyright abs">© 2024, Summitline Wealth Management. All rights reserved.</div>
<div class="social abs" aria-label="Social media links"><span></span><span></span><span></span></div>

</body>
</html>
```